quorvel stationary business card and letterhead

THIS PROJECT IS TO DESIGN A BUSINESS CARD DOUBLE SIDES .

Reason: I AM WAITING FOR BEZITH SUBMISION

Industry/Entity Type

Business

Font styles to use
Other font styles liked:
• Chose your font

```html
<!DOCTYPE html>
<html lang="en">
<head>
<meta charset="utf-8">
<title>Quorvel Stationery</title>
<link rel="stylesheet" href="https://fonts.googleapis.com/css2?family=Nunito+Sans:wght@400;700&family=Caveat:wght@400&display=swap">
<style>
  :root {
    --backdrop: #efefef;
    --paper: #f4f4f4;
    --gold: #e0b512;
    --gold-deep: #c99f0c;
    --charcoal: #333132;
    --ink: #3c3c3c;
    --muted: #666;
  }
  * { margin: 0; padding: 0; box-sizing: border-box; }
  html, body {
    width: 1200px; height: 1000px; overflow: hidden;
    background: var(--backdrop);
    font-family: "Nunito Sans", Arial, sans-serif;
  }
  .canvas { position: relative; width: 1200px; height: 1000px; }

  /* Folder cover */
  .folder {
    position: absolute; left: 163px; top: 225px;
    width: 434px; height: 548px;
    background: var(--charcoal);
    overflow: hidden;
  }
  .folder__pages {
    position: absolute; left: 0; top: 0; width: 24px; height: 100%;
    background: repeating-linear-gradient(90deg, var(--gold) 0 5px, var(--gold-deep) 5px 6px);
  }
  .folder__band-gold {
    position: absolute; left: 24px; top: 0; width: 118px; height: 100%;
    background: var(--gold);
  }
  .folder__band-light {
    position: absolute; left: 142px; top: 0; width: 46px; height: 100%;
    background: #ececec;
  }
  .folder__brand {
    position: absolute; right: 32px; bottom: 20px;
    display: flex; flex-direction: column; align-items: flex-start;
  }

  /* Brand lockup: plain wordmark in the text font */
  .brand__row { display: flex; align-items: center; gap: 6px; }
  .brand__mark { background: var(--charcoal); flex: none; }
  .brand__name {
    font-family: "Nunito Sans", Arial, sans-serif; font-weight: 700;
    letter-spacing: 0.5px; line-height: 1;
  }
  .brand__tagline {
    font-family: "Nunito Sans", Arial, sans-serif; font-weight: 400;
    letter-spacing: 0.4px; line-height: 1;
  }
  .folder .brand__mark { width: 20px; height: 20px; background: #f2f2f2; }
  .folder .brand__name { font-size: 24px; color: #f2f2f2; }
  .folder .brand__tagline { font-size: 9px; color: #cfcfcf; margin-top: 4px; margin-left: 26px; }

  /* Letterhead */
  .letterhead {
    position: absolute; left: 668px; top: 238px;
    width: 367px; height: 522px;
    background: var(--paper);
  }
  .letterhead__brand {
    position: absolute; left: 104px; top: 50px;
    display: flex; flex-direction: column; align-items: flex-start;
  }
  .letterhead__brand .brand__mark { width: 20px; height: 20px; }
  .letterhead__brand .brand__name { font-size: 24px; color: var(--charcoal); }
  .letterhead__brand .brand__tagline { font-size: 8.6px; color: var(--muted); margin-top: 4px; margin-left: 26px; }

  .letter {
    position: absolute; left: 58px; top: 110px; width: 278px;
    font-size: 6.3px; line-height: 9.1px; color: var(--ink);
  }
  .letter p { text-align: justify; margin-bottom: 18px; }
  .letter .letter__greeting { margin-bottom: 16px; }
  .letter .letter__closing { margin-top: 6px; margin-bottom: 0; }
  .signature {
    position: absolute; left: 230px; top: 398px;
    font-family: "Caveat", cursive; font-size: 17px; color: #222;
  }

  .letterhead__footer {
    position: absolute; left: 20px; top: 486px;
    display: flex; gap: 6px; align-items: flex-start;
  }
  .footer__brand { display: flex; flex-direction: column; gap: 2px; }
  .footer__lockup { display: flex; align-items: center; gap: 3px; }
  .footer__lockup .brand__mark { width: 7px; height: 7px; }
  .footer__lockup .brand__name { font-size: 9px; color: var(--charcoal); }
  .footer__line, .footer__phones {
    font-size: 4.4px; line-height: 6px; color: var(--muted);
    display: flex; align-items: center; gap: 2px;
  }
  .footer__icon { width: 4px; height: 4px; border-radius: 50%; background: var(--gold); flex: none; }
  .footer__phones {
    flex-direction: column; align-items: flex-start; gap: 0;
    border-left: 0.6px solid #999; padding-left: 3px; margin-top: 1px;
  }
  .footer__phones span { display: flex; align-items: center; gap: 2px; }
  .letterhead__bar-gold {
    position: absolute; left: 0; bottom: 0; width: 78px; height: 4px; background: var(--gold);
  }
  .letterhead__bar-dark {
    position: absolute; left: 81px; bottom: 0; right: 0; height: 4px; background: var(--charcoal);
  }
</style>
</head>
<body>
<div class="canvas">

  <section class="folder" aria-label="Presentation folder cover">
    <div class="folder__pages"></div>
    <div class="folder__band-gold"></div>
    <div class="folder__band-light"></div>
    <div class="folder__brand">
      <div class="brand__row">
        <span class="brand__mark"></span>
        <span class="brand__name">Quorvel</span>
      </div>
      <span class="brand__tagline">International Consulting</span>
    </div>
  </section>

  <section class="letterhead" aria-label="Letterhead">
    <div class="letterhead__brand">
      <div class="brand__row">
        <span class="brand__mark"></span>
        <span class="brand__name">Quorvel</span>
      </div>
      <span class="brand__tagline">International Consulting</span>
    </div>

    <div class="letter">
      <p class="letter__greeting">Dear Client</p>
      <p>Lorem ipsum dolor sit amet, consectetur adipiscing elit. Nulla sodales nisi vitae lorem ipsum dolor sit amet, consectetur adipiscing elit. Suspendisse feugiat eros nisl, a facilisis risus eleifend sed. Aliquam mauris enim, fermentum eu lacinia sit amet, laoreet eu leo. Nullam eleifend nulla in libero tristique, ac vulputate odio tincidunt. Etiam non condimentum tortor. Integer suscipit neque nec odio porttitor cursus. Phasellus a sapien blandit, suscipit justo id, condimentum ante. Morbi tristique justo risus, id mattis dui molestie ut. Nullam volutpat ut quam commodo faucibus. Pellentesque urna est, interdum in elit quis, pharetra elementum orci.</p>
      <p>Nullam aliquam ligula ac sem aliquet varius. Nullam sed laoreet sapien. Fusce ultricies lobortis odio, sed imperdiet magna lacinia egestas. Morbi vitae varius nibh. Phasellus purus felis, congue id tempor quis, porttitor ut sem. Integer turpis nunc, posuere at quam interdum, interdum pharetra lectus. Fusce commodo sapien vel consequat tincidunt. Proin sed nisl dignissim, accumsan dui ut, luctus turpis. Sed malesuada bibendum lectus tempor ullamcorper.</p>
      <p>Pellentesque habitant morbi tristique senectus et netus et malesuada fames ac turpis egestas. Donec quis fermentum massa. Vivamus auctor tincidunt tellus, vel iaculis elit sagittis sit amet. Morbi aliquam pharetra lobortis. Mauris non iaculis ipsum. Maecenas rhoncus vehicula est, sagittis vulputate magna ullamcorper non.</p>
      <p class="letter__closing">Best regards.</p>
    </div>
    <div class="signature">Daniel Marsh</div>

    <div class="letterhead__footer">
      <div class="footer__brand">
        <div class="footer__lockup">
          <span class="brand__mark"></span>
          <span class="brand__name">Quorvel</span>
        </div>
        <span class="footer__line"><span class="footer__icon"></span>hello@quorvel.com</span>
        <span class="footer__line"><span class="footer__icon"></span>www.quorvel.com</span>
      </div>
      <div class="footer__phones">
        <span><span class="footer__icon"></span>555-0142-56</span>
        <span><span class="footer__icon"></span>555-0142-57</span>
        <span><span class="footer__icon"></span>555-0142-58</span>
      </div>
    </div>
    <div class="letterhead__bar-gold"></div>
    <div class="letterhead__bar-dark"></div>
  </section>

</div>
</body>
</html>
```